" A Quitavel é uma empresa que desenvolve e fornece o sistema de cobrança Quitavel para empresas de cobrança (escritórios de cobrança, assessorias de cobranças, escritórios de advogados), tais clientes chamamos de ASSESSORIAS, e também fornecemos o sistema para empresas que possuem uma grande quantidade de clientes inadimplentes e que fazem a cobrança destes clientes internamente através de um departamento de cobrança, estes clientes chamamos de CREDORES. Alguns clientes ASSESSORIAS: www.grupoltn-exemplo.com.br www.moraisetavares-exemplo.com.br www.rvrecupera-exemplo.com.br Alguns clientes CREDORES: www.linguaviva-exemplo.com www.grupovelarium-exemplo.com.br www.ronaldos-exemplo.com.br Todos os produtos e serviços que comercializamos são através da plataforma Quitavel, por exemplo, para que um cliente utilize nosso produto “Portal de Negociação” ele precisa contratar o Quitavel já que suas configurações são através do sistema, da mesma forma o serviço de “SMS”, já que as campanhas são criadas e disparadas pelo sistema Quitavel. O sistema Quitavel “nasceu” primeiro que a empresa Quitavel, já que dois dos atuais sócios possuíram uma empresa anterior de 2012 até a abertura da Quitavel em 1 de setembro de 2015. Esta empresa desenvolvia um sistema focado para assessorias de cobrança, porém em uma tecnologia antiga, e então resolveram criar um novo software com tecnologias atuais na época e para isto buscaram um investidor e juntos optaram por criar uma nova empresa, uma nova marca. Nossa logo foi construída através da plataforma Marca Pronta e gostamos muito do resultado! E estamos aqui novamente buscando que seus profissionais nos ajudem a criar novos materiais que hoje se fazem necessários para nós. "

```html
<!DOCTYPE html>
<html lang="pt-BR">
<head>
<meta charset="utf-8">
<title>Quitavel — Sobre nós</title>
<link rel="stylesheet" href="https://fonts.googleapis.com/css2?family=Open+Sans:wght@400;600;700;800&display=swap">
<style>
  :root {
    --page-bg: #eef0f3;
    --slide-bg: #ffffff;
    --navy: #1f2f86;
    --navy-dark: #16236b;
    --box-blue: #2c3f98;
    --text: #4a4d55;
    --heading: #2b2d33;
    --city-top: rgba(200, 206, 216, 0);
    --city-mid: rgba(184, 192, 205, 0.55);
    --city-low: rgba(214, 219, 227, 0.7);
  }
  * { margin: 0; padding: 0; box-sizing: border-box; }
  html, body { width: 1200px; height: 1200px; overflow: hidden; }
  body {
    background: var(--page-bg);
    font-family: "Open Sans", sans-serif;
    display: flex; align-items: center; justify-content: center;
  }
  .slide {
    position: relative;
    width: 1120px; height: 644px;
    background: var(--slide-bg);
    overflow: hidden;
    box-shadow: 0 6px 30px rgba(0,0,0,0.12);
  }
  .slide__band {
    position: absolute; left: 0; top: 0; bottom: 0; width: 34px;
    background: linear-gradient(90deg, var(--navy-dark) 0 60%, var(--navy) 60% 100%);
  }
  .slide__city {
    position: absolute; left: 34px; right: 0; top: 300px; height: 250px;
    background: linear-gradient(180deg, var(--city-top) 0%, var(--city-mid) 45%, var(--city-low) 100%);
  }
  .about {
    position: absolute; left: 95px; top: 92px; width: 480px;
    color: var(--text); font-size: 12.5px; line-height: 1.55;
  }
  .about__title {
    font-size: 21px; font-weight: 700; color: var(--heading);
    letter-spacing: 0.3px; margin-bottom: 16px;
  }
  .about p { margin-bottom: 15px; }
  .stats {
    position: absolute; left: 631px; top: 129px; width: 439px;
    display: grid; grid-template-columns: 213px 213px; gap: 10px 13px;
  }
  .stat {
    background: var(--box-blue); color: #fff;
    height: 50px; display: flex; align-items: center; justify-content: center;
    font-size: 14px; font-weight: 600; letter-spacing: 0.2px;
  }
  .year-data {
    position: absolute; left: 631px; top: 256px; width: 439px; min-height: 214px;
    background: var(--box-blue); color: #fff;
    padding: 18px 22px 16px; font-size: 13.5px; font-weight: 600; line-height: 1.3;
  }
  .year-data__title { margin-bottom: 16px; }
  .year-data ul { list-style: none; }
  .year-data li { margin-bottom: 9px; padding-left: 16px; text-indent: -16px; }
  .year-data li:last-child { margin-bottom: 0; }
  .year-data li.growth { padding-left: 0; text-indent: 0; margin-left: 16px; }
  .brand {
    position: absolute; right: 44px; bottom: 20px;
    display: flex; align-items: center; gap: 7px;
    font-size: 24px; font-weight: 700; color: var(--navy);
  }
  .brand__dot { width: 12px; height: 12px; border-radius: 50%; background: var(--navy); }
</style>
</head>
<body>
  <section class="slide">
    <div class="slide__band"></div>
    <div class="slide__city" role="img" aria-label="Foto esmaecida de horizonte urbano com prédios"></div>

    <div class="about">
      <h1 class="about__title">SOBRE NÓS</h1>
      <p>Somos uma empresa de tecnologia especializada em desenvolver ferramentas e serviços para empresas e departamentos de cobrança.</p>
      <p>Nosso propósito tem sido fornecer o melhor sistema de cobrança do mercado para ajudar nossos clientes a conquistarem cada vez mais resultados nas negociações de dívidas com seus clientes e contribuir para que mais pessoas possam recuperar o seu crédito.</p>
      <p>Nossa equipe é experiente e atua desde 2006 neste mercado. Sabemos que para prosperar é preciso ter uma base sólida e trabalhar muito. E foi desta maneira que criamos nossa plataforma de cobrança.</p>
      <p>Estávamos inconformados com sistemas existentes no mercado, ultrapassados em tecnologia e usabilidade, e foi esta a motivação somada com vontade e fazer mais e melhor que nos levou a trabalhar muito duro para criar do zero e com o que há de mais moderno em tecnologia da informação o sistema de cobrança mais inovador do mercado!</p>
    </div>

    <div class="stats">
      <div class="stat">+ DE 20 PARCEIROS</div>
      <div class="stat">+ DE 150 ASSESSORIAS</div>
      <div class="stat">+ DE 2000 CREDORES</div>
      <div class="stat">+ DE 1500 USUÁRIOS</div>
    </div>

    <div class="year-data">
      <div class="year-data__title">DADOS DE 2017</div>
      <ul>
        <li class="growth">130% DE CRESCIMENTO</li>
        <li>+ DE 1 MILHÃO DE CLIENTES COM ACORDOS PAGOS</li>
        <li>+ DE 750 MILHÕES DE REAIS DE DÍVIDAS RECEBIDAS</li>
        <li>+ DE 30 MILHÕES DE REAIS EM RECEITAS GERADAS<br>PARA AS ASSESSORIAS</li>
      </ul>
    </div>

    <div class="brand"><span class="brand__dot"></span>Quitavel</div>
  </section>
</body>
</html>
```